Corvane Business Cards & Staionary
Corvane, Inc.
Project: Corvane Business Cards & Staionary
Corvane Business Cards & Staionary - Real Estate
Creative Brief
Professional
Leonard T. Haskovich
President
418 W. Thornberry Blvd. Harlow Springs, TX 75482
len@corvanetx.com

```html
<!DOCTYPE html>
<html lang="en">
<head>
<meta charset="utf-8">
<title>Corvane, Inc. Business Cards</title>
<link href="https://fonts.googleapis.com/css2?family=Cormorant+Garamond:wght@500;600;700&display=swap" rel="stylesheet">
<style>
  :root {
    --backdrop-light: #eceded;
    --backdrop-dark: #c9cacc;
    --gold: #c9951f;
    --gold-light: #e9b83a;
    --gold-deep: #a87812;
    --charcoal: #4a4a4c;
    --ink: #3a3a3c;
    --paper: #ffffff;
  }
  * { margin: 0; padding: 0; box-sizing: border-box; }
  html, body { width: 1200px; height: 984px; overflow: hidden; }
  body {
    background: radial-gradient(ellipse at 50% 40%, var(--backdrop-light) 0%, var(--backdrop-dark) 100%);
    font-family: "Cormorant Garamond", Georgia, serif;
    color: var(--ink);
    position: relative;
  }
  .card {
    position: absolute;
    left: 250px;
    width: 700px;
    height: 400px;
    border-radius: 22px;
    overflow: hidden;
    box-shadow: 0 14px 30px rgba(0,0,0,0.22);
  }
  .card--back {
    top: 60px;
    background: radial-gradient(ellipse at 60% 35%, var(--gold-light) 0%, var(--gold) 55%, var(--gold-deep) 100%);
  }
  .back-brand {
    position: absolute;
    left: 44px;
    top: 110px;
    font-size: 64px;
    font-weight: 700;
    color: var(--charcoal);
    line-height: 1;
  }
  .back-website {
    position: absolute;
    right: 40px;
    bottom: 36px;
    color: var(--paper);
    font-size: 22px;
    letter-spacing: 4px;
    font-weight: 600;
  }
  .card--front {
    top: 524px;
    background: var(--paper);
  }
  .front-swoosh { position: absolute; left: 0; bottom: 0; width: 700px; height: 400px; }
  .brand {
    position: absolute;
    top: 62px;
    left: 0;
    width: 100%;
    text-align: center;
  }
  .brand-name {
    font-size: 54px;
    font-weight: 700;
    color: var(--charcoal);
    line-height: 1;
  }
  .brand-tagline {
    font-size: 13px;
    letter-spacing: 2.5px;
    text-transform: uppercase;
    color: var(--charcoal);
    margin-top: 6px;
    font-weight: 600;
  }
  .person {
    position: absolute;
    top: 160px;
    left: 0;
    width: 100%;
    text-align: center;
  }
  .person-name {
    font-size: 24px;
    font-variant: small-caps;
    color: var(--gold);
    letter-spacing: 1.5px;
    font-weight: 600;
  }
  .person-title {
    font-size: 17px;
    font-variant: small-caps;
    color: var(--charcoal);
    letter-spacing: 1px;
  }
  .address {
    position: absolute;
    top: 226px;
    right: 372px;
    text-align: right;
    font-size: 17px;
    font-style: normal;
    font-variant: small-caps;
    line-height: 1.35;
    color: var(--charcoal);
    font-weight: 600;
  }
  .contact-list {
    position: absolute;
    top: 222px;
    left: 352px;
    list-style: none;
    font-size: 16px;
    line-height: 1.42;
    color: var(--charcoal);
    font-weight: 600;
    border-left: 1px solid var(--gold);
    padding-left: 10px;
  }
  .contact-list li { display: flex; align-items: center; gap: 8px; }
  .contact-icon {
    width: 11px; height: 11px;
    background: var(--gold);
    border-radius: 2px;
    flex: none;
  }
</style>
</head>
<body>
  <section class="card card--back" aria-label="Business card back">
    <p class="back-brand">Corvane</p>
    <p class="back-website">WWW.CORVANETX.COM</p>
  </section>

  <section class="card card--front" aria-label="Business card front">
    <svg class="front-swoosh" viewBox="0 0 700 400" aria-hidden="true">
      <defs>
        <linearGradient id="goldBand" x1="0" y1="0" x2="1" y2="0">
          <stop offset="0" stop-color="#e9b83a"/>
          <stop offset="0.5" stop-color="#c9951f"/>
          <stop offset="1" stop-color="#a87812"/>
        </linearGradient>
      </defs>
      <path d="M0 300 C180 330 420 350 700 296 L700 400 L0 400 Z" fill="url(#goldBand)"/>
      <path d="M0 312 C200 342 440 356 700 318 L700 340 C440 372 200 360 0 336 Z" fill="#4a4a4c"/>
      <path d="M0 328 C220 358 460 366 700 334 L700 346 C460 378 220 372 0 344 Z" fill="#ffffff"/>
    </svg>

    <div class="brand">
      <p class="brand-name">Corvane, Inc.</p>
      <p class="brand-tagline">Property Management Company</p>
    </div>

    <div class="person">
      <p class="person-name">Leonard T. Haskovich</p>
      <p class="person-title">President</p>
    </div>

    <address class="address">
      418 W. Thornberry Blvd.<br>
      Harlow Springs, TX 75482
    </address>

    <ul class="contact-list">
      <li><span class="contact-icon"></span>(512) 555-0142</li>
      <li><span class="contact-icon"></span>(512) 555-0143</li>
      <li><span class="contact-icon"></span>len@corvanetx.com</li>
      <li><span class="contact-icon"></span>www.corvanetx.com</li>
    </ul>
  </section>
</body>
</html>
```